8 Page Publishing/Entertainment Website Design

We need a slick, polished, professional looking fully mobile responsive website designed for the publishing / entertainment industry. It will contain 8 pages, including the Home page. The site is to be designed in pure HTML and CSS only and to be compatible with any type of server we put it on. Pages are *not* to be part of any template system, like WordPress or others like it. Pure HTML and CSS standalone pages only. No WordPress or Joomla, etc. Website to use our logo's colors of red/white throughout its design. Uploaded files contain a word DOC that outlines more of our needs and we have included our logo file. Please read the specifications in the Word Document attached. We have also included a PDF file with the website specs as well.

Target Market(s)

Authors and Screenwriters

Coding

Coded - Design and coding required

Number of Pages Required

5+ page

Colors
ec1f27
ffffff
f04a50
f59195

Requirements
Must have
• The site is to be designed in pure HTML and CSS only and to be compatible with any type of server we put it on. Pages are *not* to be part of any template system, like WordPress or others like it. Pure HTML and CSS standalone pages only. No WordPress or Joomla, etc. Website to use our logo's colors of red/white throughout its design. Uploaded files contain a word DOC that outlines more of our needs and we have included our logo file. Please read the specifications in the Word Document attached. We have also included a PDF file with the website specs as well.
Should not have
• No Wordpress or other Template type pages. Pure HTML and CSS only. Some Javascript and JQuery is okay, upon approval.

```html
<!DOCTYPE html>
<html lang="en">
<head>
<meta charset="utf-8">
<title>Northlight Press — Home</title>
<link href="https://fonts.googleapis.com/css2?family=Oswald:wght@400;500;600&family=Nunito+Sans:wght@400;600;700&display=swap" rel="stylesheet">
<style>
:root{
  --red:#ec1f27;
  --red-soft:#f04a50;
  --pink:#f59195;
  --white:#ffffff;
  --ink:#111111;
  --text:#333333;
  --grey:#a5a5a5;
  --grey-light:#ececec;
  --black:#000000;
}
*{box-sizing:border-box;margin:0;padding:0}
html,body{width:1200px;height:3186px;overflow:hidden}
body{position:relative;background:var(--white);font-family:"Nunito Sans",Arial,sans-serif;color:var(--text)}
.abs{position:absolute}
.heading{font-family:"Oswald",Impact,sans-serif;font-weight:500;color:var(--ink);text-transform:uppercase;text-align:center;letter-spacing:.5px}
.btn{position:absolute;background:var(--red);color:var(--white);font-size:17px;letter-spacing:3px;text-transform:uppercase;display:flex;align-items:center;justify-content:center}

/* nav */
.site-nav{top:0;left:0;width:1200px;height:53px;background:var(--white);z-index:3}
.site-nav a{position:absolute;top:18px;font-size:12px;letter-spacing:1.2px;color:var(--ink);text-decoration:none;font-weight:600}
.brand-badge{position:absolute;left:549px;top:0;width:104px;height:104px;border-radius:50%;background:var(--white);border:5px solid var(--red);z-index:4;display:flex;align-items:center;justify-content:center;text-align:center;font-family:"Oswald",sans-serif;font-weight:500;font-size:13px;line-height:1.15;color:var(--red);letter-spacing:1px}

/* hero */
.hero{top:53px;left:0;width:1200px;height:467px;background:linear-gradient(180deg,#6f8aa6 0%,#8a9fb4 35%,#4e5660 70%,#1d1f22 100%)}
.hero-title{left:87px;top:202px;font-family:"Oswald",sans-serif;font-weight:500;font-size:44px;line-height:1;color:var(--white);padding-left:18px;border-left:5px solid var(--red);letter-spacing:-.3px}
.hero-lead{left:87px;top:264px;width:420px;font-size:15px;line-height:22px;color:var(--white)}
.hero-video{left:743px;top:130px;width:370px;height:316px;border:4px solid var(--red);background:linear-gradient(160deg,#c9d6e3,#e9e2d6 50%,#b7c2cc)}
.play{position:absolute;left:148px;top:125px;width:64px;height:64px;border-radius:50%;background:var(--red)}

/* about */
.about-title{top:582px;left:0;width:1200px;font-size:38px}
.about-text{top:640px;left:102px;width:996px;font-size:13px;line-height:24px;text-align:center;color:#333}

/* worlds */
.worlds-band{top:871px;left:0;width:1200px;height:297px;background:linear-gradient(90deg,#5c5f66,#6e7077 50%,#4d5057)}
.worlds-title{top:930px;left:0;width:1200px;font-size:38px;color:var(--white)}
.world-card{top:998px;width:291px;height:387px;background:#f1f1f1;box-shadow:0 4px 14px rgba(0,0,0,.25)}
.world-cover{position:absolute;left:29px;top:28px;width:221px;height:333px;box-shadow:4px 6px 10px rgba(0,0,0,.3)}
.world-name{top:1407px;width:291px;text-align:center;font-family:"Oswald",sans-serif;font-weight:500;font-size:17px;color:var(--ink)}
.world-desc{top:1440px;width:291px;text-align:center;font-size:13px;line-height:24px}
.world-link{top:1492px;width:291px;text-align:center;font-size:13px;color:var(--red);text-decoration:underline}

/* authors */
.authors{top:1580px;left:0;width:1200px;height:482px;background:linear-gradient(90deg,#f3e3cf 0%,#f7ece4 40%,#f4e4e4 75%,#f0dada 100%)}
.authors-title{top:1660px;left:0;width:1200px;font-size:38px}
.authors-text{top:1719px;left:296px;width:608px;text-align:center;font-size:13px;line-height:24px}
.avatar{top:1821px;width:80px;height:80px;border-radius:50%;background:linear-gradient(160deg,#d9cfc8,#8d8680);border:3px solid var(--white);box-shadow:0 2px 6px rgba(0,0,0,.2)}
.quill{top:1600px;left:950px;width:120px;height:428px;background:linear-gradient(180deg,#f04a50 0%,#ec1f27 55%,#3b4150 80%,#23272f 100%);border-radius:60px 60px 20px 20px}

/* faq */
.faq-title{top:2126px;left:0;width:1200px;font-size:38px}
.faq-panel{top:2198px;left:87px;width:1026px;height:340px;background:var(--white);box-shadow:0 2px 16px rgba(0,0,0,.18)}
.faq-q{position:absolute;width:473px;height:40px;background:var(--grey);color:var(--white);font-size:15px;padding:0 16px;display:flex;align-items:center;justify-content:space-between}
.faq-q.open{background:var(--red)}
.faq-a{position:absolute;left:26px;top:166px;width:473px;height:115px;background:var(--grey-light);padding:12px 16px;font-size:12.5px;line-height:23px;color:#333}

/* footer */
.footer{top:2627px;left:0;width:1200px;height:457px;background:var(--black)}
.foot-title{position:absolute;font-family:"Oswald",sans-serif;font-weight:500;font-size:21px;color:var(--white);text-transform:uppercase}
.field{position:absolute;background:var(--white);font-size:12px;color:#333;padding:10px}
.divider{position:absolute;left:709px;top:70px;width:1px;height:320px;background:#333}
.info-row{position:absolute;left:830px;display:flex;align-items:center;gap:18px;color:var(--white);font-size:13px;line-height:22px}
.info-icon{width:34px;height:34px;border-radius:50%;background:var(--white);display:flex;align-items:center;justify-content:center;flex:none}
.social{position:absolute;top:302px;width:46px;height:46px;border-radius:50%;background:var(--red)}
.to-top{position:absolute;left:1098px;top:384px}

/* bottom bar */
.bottom{top:3084px;left:0;width:1200px;height:102px;background:var(--white)}
.bottom-brand{position:absolute;left:87px;top:17px;width:68px;height:68px;border-radius:50%;border:4px solid var(--red);display:flex;align-items:center;justify-content:center;text-align:center;font-family:"Oswald",sans-serif;font-weight:500;font-size:9px;line-height:1.15;color:var(--red)}
.bottom-links{position:absolute;left:250px;top:42px;font-size:13px;color:#222}
.bottom-copy{position:absolute;right:87px;top:42px;font-size:13px;color:#222}
</style>
</head>
<body>

<nav class="abs site-nav">
  <a style="left:178px">ABOUT NP</a>
  <a style="left:282px">APPLY NOW</a>
  <a style="left:384px">NP WORLDS</a>
  <a style="left:728px">NP AUTHORS</a>
  <a style="left:850px">FAQ</a>
  <a style="left:902px">NEWS</a>
  <a style="left:966px">CONTACT US</a>
</nav>
<div class="brand-badge">NORTHLIGHT<br>PRESS</div>

<section class="abs hero" role="img" aria-label="Rocket launching with clouds of smoke at dusk"></section>
<h1 class="abs hero-title">LOREM IPSUM DUMMY</h1>
<p class="abs hero-lead">It is a long established fact that a reader will be distracted by the readable content of a page.</p>
<div class="btn" style="left:87px;top:321px;width:412px;height:42px">Apply Now</div>
<div class="abs hero-video" role="img" aria-label="Video preview of an open book with coloured tabs">
  <div class="play"><svg width="64" height="64" viewBox="0 0 64 64"><path d="M26 20 L46 32 L26 44 Z" fill="#1a1a1a"/></svg></div>
</div>

<h2 class="abs heading about-title">About NP</h2>
<p class="abs about-text">There are many variations of passages of Lorem Ipsum available, but the majority have suffered alteration in some form, by injected humour, or randomised words which don't look even slightly believable. If you are going to use a passage of Lorem Ipsum, you need to be sure there isn't anything embarrassing hidden in the middle of text. All the Lorem Ipsum generators on the Internet tend to repeat predefined chunks as necessary, making this the first true generator on the Internet. It uses a dictionary of over 200 Latin words, combined with a handful of model sentence structures, to generate Lorem Ipsum which looks reasonable.</p>
<div class="btn" style="left:499px;top:758px;width:202px;height:41px">Read More</div>

<section class="abs worlds-band" role="img" aria-label="Close-up of stacked books"></section>
<h2 class="abs heading worlds-title">NP Worlds</h2>

<div class="abs world-card" style="left:149px"><div class="world-cover" role="img" aria-label="Book cover with pink and blue paint strokes" style="background:linear-gradient(160deg,#2f3766 0%,#e9d8b8 35%,#e7659a 70%,#7cc6d6 100%)"></div></div>
<div class="abs world-card" style="left:455px"><div class="world-cover" role="img" aria-label="Book cover with pink brush strokes on plum" style="background:linear-gradient(170deg,#e5747f 0%,#d2566f 40%,#5b2f55 100%)"></div></div>
<div class="abs world-card" style="left:760px"><div class="world-cover" role="img" aria-label="Purple book cover with yellow paint swirls" style="background:linear-gradient(160deg,#5a3c86 0%,#7a4c8c 45%,#e8c46a 70%,#5a3c86 100%)"></div></div>

<div class="abs world-name" style="left:149px">LOREM IPSUM</div>
<div class="abs world-name" style="left:455px">THE STANDARD CHUNK</div>
<div class="abs world-name" style="left:760px">CONTRARY POPULAR</div>
<p class="abs world-desc" style="left:149px">Lorem Ipsum available, but the majority have<br>suffered alteration in some form</p>
<p class="abs world-desc" style="left:455px">Lorem Ipsum available, but the majority have<br>suffered alteration in some form</p>
<p class="abs world-desc" style="left:760px">Lorem Ipsum available, but the majority have<br>suffered alteration in some form</p>
<a class="abs world-link" style="left:149px">VIEW DETAILS</a>
<a class="abs world-link" style="left:455px">VIEW DETAILS</a>
<a class="abs world-link" style="left:760px">VIEW DETAILS</a>

<section class="abs authors" role="img" aria-label="Soft background of books and paper"></section>
<div class="abs quill" role="img" aria-label="Red quill pen in an ink bottle"></div>
<h2 class="abs heading authors-title">NP Authors</h2>
<p class="abs authors-text">Lorem ipsum dolor sit amet, consectetur adipiscing elit, sed do eiusmod tempor incididunt ut labore et dolore magna aliqua. Ut enim ad minim veniam, quis nostrud exercitation ullamco laboris nisi ut aliquip ex ea commodo consequat. Duis aute irure dolor in reprehenderit in voluptate velit esse.</p>
<div class="abs avatar" style="left:310px" role="img" aria-label="Author portrait"></div>
<div class="abs avatar" style="left:436px" role="img" aria-label="Author portrait"></div>
<div class="abs avatar" style="left:561px" role="img" aria-label="Author portrait"></div>
<div class="abs avatar" style="left:684px" role="img" aria-label="Author portrait"></div>
<div class="abs avatar" style="left:810px" role="img" aria-label="Author portrait"></div>
<div class="btn" style="left:501px;top:1935px;width:198px;height:40px">View Details</div>

<h2 class="abs heading faq-title">FAQ</h2>
<section class="abs faq-panel">
  <div class="faq-q" style="left:26px;top:56px">What is Lorem Ipsum?<svg width="12" height="8" viewBox="0 0 12 8"><path d="M1 1l5 5 5-5" stroke="#fff" stroke-width="1.6" fill="none"/></svg></div>
  <div class="faq-q open" style="left:26px;top:126px">Where does it come from?<svg width="12" height="8" viewBox="0 0 12 8"><path d="M1 7l5-5 5 5" stroke="#fff" stroke-width="1.6" fill="none"/></svg></div>
  <div class="faq-a">Lorem Ipsum is simply dummy text of the printing and typesetting industry. Lorem Ipsum has been the industry's standard dummy text ever since the 1500s, when an unknown printer took a galley of type and scrambled it to make a type specimen book.</div>
  <div class="faq-q" style="left:527px;top:56px">Why do we use it?<svg width="12" height="8" viewBox="0 0 12 8"><path d="M1 1l5 5 5-5" stroke="#fff" stroke-width="1.6" fill="none"/></svg></div>
  <div class="faq-q" style="left:527px;top:126px">Where can I get some?<svg width="12" height="8" viewBox="0 0 12 8"><path d="M1 1l5 5 5-5" stroke="#fff" stroke-width="1.6" fill="none"/></svg></div>
  <div class="faq-q" style="left:527px;top:196px">What is Lorem Ipsum?<svg width="12" height="8" viewBox="0 0 12 8"><path d="M1 1l5 5 5-5" stroke="#fff" stroke-width="1.6" fill="none"/></svg></div>
</section>

<footer class="abs footer">
  <h3 class="foot-title" style="left:87px;top:68px">Contact Form</h3>
  <div class="field" style="left:87px;top:115px;width:236px;height:40px">First Name</div>
  <div class="field" style="left:350px;top:115px;width:236px;height:40px">Last Name</div>
  <div class="field" style="left:87px;top:179px;width:236px;height:40px">Phone</div>
  <div class="field" style="left:350px;top:179px;width:236px;height:40px">Email</div>
  <div class="field" style="left:87px;top:240px;width:499px;height:85px">Message</div>
  <div class="btn" style="left:87px;top:347px;width:198px;height:40px">Submit</div>

  <div class="divider"></div>

  <h3 class="foot-title" style="left:830px;top:68px">Contact Info</h3>
  <div class="info-row" style="top:116px">
    <span class="info-icon"><svg width="16" height="18" viewBox="0 0 16 18"><path d="M8 1a6 6 0 0 0-6 6c0 4.5 6 10 6 10s6-5.5 6-10a6 6 0 0 0-6-6z" fill="#ec1f27"/><circle cx="8" cy="7" r="2.2" fill="#fff"/></svg></span>
    <span>123 Street, Lorem Ipsum dummy text.<br>New York, USA 123456</span>
  </div>
  <div class="info-row" style="top:180px">
    <span class="info-icon"><svg width="16" height="16" viewBox="0 0 16 16"><path d="M3.5 1.5l2.5 0 1 3.5-1.8 1.2a9 9 0 0 0 4.6 4.6L11 9l3.5 1v2.5c0 1-1 2-2 2C6.5 14.5 1.5 9.5 1.5 3.5c0-1 1-2 2-2z" fill="#ec1f27"/></svg></span>
    <span>9876 543 210 &nbsp;/&nbsp; 1234 567 890</span>
  </div>
  <div class="info-row" style="top:240px">
    <span class="info-icon"><svg width="16" height="12" viewBox="0 0 16 12"><rect x="0.5" y="0.5" width="15" height="11" rx="1.5" fill="#ec1f27"/><path d="M1 1.5l7 5 7-5" stroke="#fff" stroke-width="1.3" fill="none"/></svg></span>
    <span>contact@northlightpress.com</span>
  </div>
  <span class="social" style="left:829px" aria-label="Social link"></span>
  <span class="social" style="left:888px" aria-label="Social link"></span>
  <span class="social" style="left:946px" aria-label="Social link"></span>

  <svg class="to-top" width="56" height="30" viewBox="0 0 56 30"><path d="M2 28 L28 3 L54 28" stroke="#555" stroke-width="2" fill="none"/></svg>
</footer>

<div class="abs bottom">
  <div class="bottom-brand">NORTHLIGHT<br>PRESS</div>
  <div class="bottom-links">Home &nbsp;|&nbsp; About NP &nbsp;|&nbsp; Apply Now &nbsp;|&nbsp; NP Worlds &nbsp;|&nbsp; NP Authors &nbsp;|&nbsp; FAQ &nbsp;|&nbsp; News &nbsp;|&nbsp; Contact us</div>
  <div class="bottom-copy">Copyright 2018 &nbsp;|&nbsp; All Rights Reserved.</div>
</div>

</body>
</html>
```